GLOW RIDGE 21 DAY Challange

looking to make a poster that needs to be 36" wide x24"tall design graphic . Check out the added file as it is a rough draft of the material I would like it to say.

Phone number 555-302-4418 www.rgchiropractic..com

Adults aged 25-45 high income adults needing to make changes in dies and lose weight

```html
<!DOCTYPE html>
<html lang="en">
<head>
<meta charset="UTF-8">
<title>Glow Ridge 21 Day Challange</title>
<link href="https://fonts.googleapis.com/css2?family=Questrial&display=swap" rel="stylesheet">
<style>
  :root {
    --stage: #e4e4e6;
    --paper: #ffffff;
    --red: #e5262c;
    --navy: #2b2f8c;
    --footer: #f4f2f4;
    --photo-light: #f3f1f0;
    --photo-mid: #e2d8d4;
    --photo-deep: #8e1a3a;
  }
  * { box-sizing: border-box; margin: 0; padding: 0; }
  html, body { width: 1200px; height: 900px; overflow: hidden; }
  body {
    background: var(--stage);
    font-family: "Questrial", "Helvetica Neue", Arial, sans-serif;
    position: relative;
  }
  .poster {
    position: absolute;
    left: 30px; top: 70px;
    width: 1140px; height: 760px;
    background: var(--paper);
    overflow: hidden;
    box-shadow: 0 10px 30px rgba(0,0,0,0.18);
  }
  .photo {
    position: absolute;
    left: 0; top: 0;
    width: 610px; height: 760px;
    background: linear-gradient(160deg, var(--photo-light) 0%, var(--photo-mid) 50%, var(--photo-deep) 100%);
  }
  .brand {
    position: absolute;
    right: 30px; top: 40px;
    display: flex; align-items: center; gap: 10px;
    color: var(--navy);
    font-size: 27px;
    letter-spacing: 1px;
    white-space: nowrap;
  }
  .brand-mark { width: 18px; height: 18px; background: var(--red); border-radius: 50%; }
  .challenge {
    position: absolute;
    left: 640px; top: 105px;
    width: 500px; height: 120px;
    background: var(--red);
    color: #fff;
    display: flex; align-items: center;
    padding: 0 20px;
    gap: 18px;
  }
  .challenge-title { font-size: 26px; line-height: 1.15; font-weight: 400; white-space: nowrap; }
  .challenge-title .big { font-size: 34px; display: block; }
  .challenge-list { list-style: none; font-size: 9.5px; line-height: 1.5; letter-spacing: 0.3px; white-space: nowrap; }
  .challenge-list .gap { margin-top: 6px; }
  .questions {
    position: absolute;
    right: 30px; top: 250px;
    display: flex; flex-direction: column; align-items: flex-end; gap: 12px;
  }
  .question {
    background: var(--navy);
    color: #fff;
    font-size: 18px;
    height: 38px;
    line-height: 38px;
    padding: 0 10px;
    letter-spacing: 0.3px;
    white-space: nowrap;
  }
  .cta {
    position: absolute;
    right: 30px; top: 502px;
    text-align: right;
  }
  .cta-main { color: var(--red); font-size: 40px; line-height: 1.05; }
  .cta-sub { color: var(--navy); font-size: 20px; margin-top: 8px; letter-spacing: 0.5px; }
  .footer {
    position: absolute;
    left: 0; bottom: 0;
    width: 1140px; height: 90px;
    background: var(--footer);
    display: flex; align-items: center; justify-content: space-between;
    padding: 0 30px 0 40px;
  }
  .address { color: var(--navy); font-size: 16px; line-height: 1.5; }
  .address .web { color: var(--red); font-size: 17px; }
  .contact {
    position: relative;
    display: flex; align-items: center; gap: 8px;
    border: 1.5px solid var(--red);
    border-radius: 6px;
    padding: 7px 14px 5px 10px;
    color: var(--navy);
    font-size: 24px;
    white-space: nowrap;
  }
  .contact-label {
    position: absolute; top: -9px; right: 12px;
    color: var(--red); font-size: 12px; line-height: 16px;
    background: var(--footer);
    padding: 0 4px;
  }
</style>
</head>
<body>
  <main class="poster">
    <div class="photo" role="img" aria-label="Photo of a man in a maroon sweater and white trousers sitting on the floor holding his ankle"></div>

    <div class="brand"><span class="brand-mark"></span>GLOW RIDGE CHIROPRACTIC</div>

    <section class="challenge">
      <h1 class="challenge-title">GLOW RIDGE 21 DAY <span class="big">CHALLANGE</span></h1>
      <ul class="challenge-list">
        <li>L - LIVES DETOX SUPPLEMENTS</li>
        <li>O - OMEGA 3 SUPPLEMENTS</li>
        <li>V - VITAMIN D SUPPLEMENTS</li>
        <li>E - EAT FRUITS &amp; VEGGIES</li>
        <li class="gap">K - Kefa Homemade Antibiotic</li>
        <li>C - Chiropatic Adjustments</li>
      </ul>
    </section>

    <section class="questions">
      <p class="question">DO YOU HAVE ALLERGIES?</p>
      <p class="question">NEED TO LOOSE WEIGHT?</p>
      <p class="question">FEEL TIRED?</p>
      <p class="question">HAVE NECK OR BACK PAIN?</p>
      <p class="question">CONTAIN WATER WEIGHT?</p>
    </section>

    <section class="cta">
      <p class="cta-main">CALL<br>TODAY!</p>
      <p class="cta-sub">FOR DETAILS</p>
    </section>

    <footer class="footer">
      <div class="address">
        <p>2870 Maple Crest Rd. Fairview, KS 66100</p>
        <p class="web">www.rgchiropractic..com</p>
      </div>
      <div class="contact">
        <span class="contact-label">Contact us</span>
        <svg width="14" height="26" viewBox="0 0 14 26" aria-hidden="true">
          <path d="M10 1 H6 Q2 1 2 6 V20 Q2 25 6 25 H10 V19 H7 V7 H10 Z" fill="#2b2f8c"/>
        </svg>
        <span>555-302-4418</span>
      </div>
    </footer>
  </main>
</body>
</html>
```